Harbourline Refrigeration business card design

We would like a new design for our business card as we have a new logo.
We need generic business card to give our customers with our office details - with the option of making it individualized for each manager

Target Market(s)

Companies and homeowners

Industry/Entity Type

Air Conditioning

Contact Information for Business Card

We are not sure if we want single or double sided it will depend on the design we choose

Colors
33a6d7
0255a3

Requirements
Must have
• Logo
• phone: (08) 8721 5940
• email: harbourserve@tealnet.example
• website: www.harbourlinerefrigeration.example
• AU61420
• BLD472913
Nice to have
• Address - Shed 5/284 Tallis Rd, Brackenridge SA 5731

```html
<!DOCTYPE html>
<html lang="en">
<head>
<meta charset="utf-8">
<title>Harbourline Refrigeration – Business Card</title>
<link rel="stylesheet" href="https://fonts.googleapis.com/css2?family=Lato:wght@400;700;900&family=Montserrat:wght@500&display=swap">
<style>
  :root {
    --navy: #16437a;
    --sky: #33a6d7;
    --ice: #8ccbea;
    --paper: #ffffff;
    --ink: #1b3f74;
    --grey: #6b6f75;
    --stage: #1c1d1f;
  }
  * { margin: 0; padding: 0; box-sizing: border-box; }
  html, body { width: 1200px; height: 852px; overflow: hidden; background: var(--stage); }
  body { font-family: "Lato", sans-serif; }
  .sheet {
    width: 1200px; height: 852px;
    display: flex; flex-direction: column; align-items: center; justify-content: center; gap: 40px;
  }
  .card {
    position: relative; width: 620px; height: 354px;
    border-radius: 18px; overflow: hidden;
  }
  /* Front */
  .card--front { background: var(--navy); display: flex; align-items: center; justify-content: center; }
  .brand { display: flex; align-items: center; gap: 14px; }
  .brand__dot { width: 26px; height: 26px; border-radius: 50%; background: currentColor; flex: none; }
  .brand__name { font-family: "Lato", sans-serif; font-weight: 900; line-height: 1.05; }
  .card--front .brand { color: var(--paper); }
  .card--front .brand__name { font-size: 40px; }
  /* Back */
  .card--back { background: var(--paper); }
  .card__waves { position: absolute; inset: 0; width: 100%; height: 100%; }
  .holder { position: absolute; right: 34px; top: 40px; text-align: right; }
  .holder__name { font-family: "Montserrat", sans-serif; font-weight: 500; font-size: 24px; color: var(--paper); letter-spacing: 0.5px; }
  .holder__role { font-size: 15px; color: var(--sky); margin-top: 2px; }
  .card--back .brand { position: absolute; left: 40px; top: 170px; color: var(--ink); gap: 10px; }
  .card--back .brand__dot { width: 18px; height: 18px; }
  .card--back .brand__name { font-size: 27px; }
  .licence { position: absolute; right: 40px; top: 224px; font-size: 14px; color: var(--ink); letter-spacing: 0.3px; }
  .rule { position: absolute; left: 40px; right: 40px; top: 248px; height: 1.5px; background: var(--ink); }
  .contacts { position: absolute; left: 40px; top: 262px; list-style: none; font-size: 14px; color: var(--grey); }
  .contacts li { display: flex; align-items: center; gap: 9px; line-height: 24px; }
  .contacts svg { width: 12px; height: 12px; fill: var(--ink); flex: none; }
  .contacts .web strong { color: var(--ink); font-weight: 400; }
  .address { position: absolute; right: 40px; top: 266px; font-style: normal; text-align: right; font-size: 14px; line-height: 22px; color: var(--grey); }
</style>
</head>
<body>
<main class="sheet">
  <section class="card card--front" aria-label="Card front">
    <div class="brand">
      <span class="brand__dot"></span>
      <span class="brand__name">Harbourline<br>Refrigeration</span>
    </div>
  </section>

  <section class="card card--back" aria-label="Card back">
    <svg class="card__waves" viewBox="0 0 620 354" preserveAspectRatio="none" aria-hidden="true">
      <path d="M0 0 H620 V138 C560 150 480 125 380 140 C250 158 110 150 0 180 Z" fill="var(--ice)"/>
      <path d="M0 0 H620 V126 C560 140 480 115 380 128 C250 145 110 135 0 162 Z" fill="var(--sky)"/>
      <path d="M0 0 H620 V112 C560 128 480 105 380 116 C250 130 110 118 0 142 Z" fill="var(--navy)"/>
    </svg>
    <div class="holder">
      <div class="holder__name">DANIEL BROOKS</div>
      <div class="holder__role">Director</div>
    </div>
    <div class="brand">
      <span class="brand__dot"></span>
      <span class="brand__name">Harbourline Refrigeration</span>
    </div>
    <div class="licence">AU61420 - BLD472913</div>
    <div class="rule"></div>
    <ul class="contacts">
      <li><svg viewBox="0 0 24 24"><path d="M6.6 10.8a15 15 0 0 0 6.6 6.6l2.2-2.2c.3-.3.7-.4 1-.2 1.1.4 2.3.6 3.6.6.6 0 1 .4 1 1V20c0 .6-.4 1-1 1A17 17 0 0 1 3 4c0-.6.4-1 1-1h3.5c.6 0 1 .4 1 1 0 1.3.2 2.5.6 3.6.1.3 0 .7-.2 1z"/></svg>(08) 8721 5940</li>
      <li><svg viewBox="0 0 24 24"><path d="M2 5h20v14H2zm2 2v.5l8 5 8-5V7zm0 2.8V17h16V9.8l-8 5z"/></svg>harbourserve@tealnet.example</li>
      <li class="web"><svg viewBox="0 0 24 24"><path d="M12 2a10 10 0 1 0 0 20 10 10 0 0 0 0-20zm6.9 6h-3a15 15 0 0 0-1.3-3.9A8 8 0 0 1 18.9 8zM12 4c.8 1.2 1.5 2.5 1.9 4h-3.8c.4-1.5 1.1-2.8 1.9-4zM4.3 14a8 8 0 0 1 0-4h3.4a16 16 0 0 0 0 4zm.8 2h3a15 15 0 0 0 1.3 3.9A8 8 0 0 1 5.1 16zm3-8h-3a8 8 0 0 1 4.3-3.9A15 15 0 0 0 8.1 8zM12 20c-.8-1.2-1.5-2.5-1.9-4h3.8c-.4 1.5-1.1 2.8-1.9 4zm2.3-6H9.7a14 14 0 0 1 0-4h4.6a14 14 0 0 1 0 4zm.3 5.9a15 15 0 0 0 1.3-3.9h3a8 8 0 0 1-4.3 3.9zm1.7-5.9a16 16 0 0 0 0-4h3.4a8 8 0 0 1 0 4z"/></svg><span>www.<strong>harbourlinerefrigeration</strong>.example</span></li>
    </ul>
    <address class="address">Shed 5/284 Tallis Rd,<br>Brackenridge SA 5731</address>
  </section>
</main>
</body>
</html>
```